The 50 Year History of the Tallowmere Whippet Coursing Society

The Tallowmere Whippet Coursing Society has been established for 50 years last month. We are putting together a chronological history book with interesting stories about events over the past 50 years.
Book title: Swift Across Decades: 50 Years of the Tallowmere Whippet Coursing Society
Front Cover: We are looking for a simple but striking design. It must have at least one racing greyhound (image from Australia). I can supply images of greyhounds if required. It must have our logo.
Back Cover: can be minimal with club details
Book Size: A4

```html
<!DOCTYPE html>
<html lang="en">
<head>
<meta charset="utf-8">
<title>Swift Across Decades – Book Cover Spread</title>
<link rel="stylesheet" href="https://fonts.googleapis.com/css2?family=Bebas+Neue&family=Archivo:wght@300;400;800&display=swap">
<style>
  :root {
    --backdrop: #d8dadb;
    --paper: #efede4;
    --ink-green: #1e4a2b;
    --club-green: #3f9a36;
    --spine-green: #34872e;
    --mark-grey: #3f5a40;
    --white: #ffffff;
    --photo-dark: #3a3c38;
    --photo-mid: #6b6a5e;
  }
  * { margin: 0; padding: 0; box-sizing: border-box; }
  html, body { width: 816px; height: 1200px; overflow: hidden; background: var(--backdrop); }
  body { font-family: "Archivo", Arial, sans-serif; }

  .spread {
    position: absolute;
    left: 8px;
    top: 324px;
    width: 800px;
    height: 552px;
    display: flex;
    box-shadow: 0 14px 30px rgba(0,0,0,0.18);
  }

  /* Back cover */
  .back-cover {
    position: relative;
    width: 390px;
    height: 552px;
    background: var(--club-green);
    color: var(--white);
    padding: 0 34px;
  }
  .back-mark {
    position: absolute;
    top: 44px;
    left: 0;
    right: 0;
    display: flex;
    justify-content: center;
    align-items: center;
    gap: 8px;
    color: var(--mark-grey);
  }
  .back-mark .dot { width: 16px; height: 16px; border-radius: 50%; background: var(--mark-grey); }
  .back-mark .name { font-weight: 800; line-height: 1.05; }
  .back-mark .name-main { display: block; font-size: 17px; }
  .back-mark .name-sub { display: block; font-size: 6px; letter-spacing: 2px; text-transform: uppercase; }

  .back-content {
    position: absolute;
    top: 104px;
    left: 34px;
    right: 34px;
    text-align: center;
  }
  .back-heading {
    font-weight: 800;
    font-size: 16px;
    line-height: 1.12;
    letter-spacing: 1.2px;
    text-transform: uppercase;
    margin-bottom: 10px;
  }
  .back-body {
    font-size: 9.5px;
    line-height: 1.35;
    font-weight: 400;
    margin-bottom: 26px;
  }
  .back-fine {
    font-size: 6.5px;
    line-height: 1.35;
    opacity: 0.85;
  }

  /* Spine */
  .spine {
    position: relative;
    width: 20px;
    height: 552px;
    background: var(--spine-green);
    box-shadow: inset 2px 0 3px rgba(0,0,0,0.15), inset -2px 0 3px rgba(0,0,0,0.15);
  }
  .spine-title {
    position: absolute;
    left: 50%;
    top: 50%;
    width: 520px;
    transform: translate(-50%, -50%) rotate(90deg);
    text-align: center;
    color: var(--white);
    font-weight: 800;
    font-size: 7.5px;
    letter-spacing: 1.2px;
    text-transform: uppercase;
    white-space: nowrap;
  }

  /* Front cover */
  .front-cover {
    position: relative;
    width: 390px;
    height: 552px;
    background: var(--paper);
    color: var(--ink-green);
  }
  .cover-title {
    position: absolute;
    left: 44px;
    top: 46px;
    font-family: "Bebas Neue", "Oswald", Impact, sans-serif;
    font-weight: 400;
    font-size: 84px;
    line-height: 0.9;
    letter-spacing: 0.5px;
  }
  .cover-title span { display: block; }
  .cover-subtitle {
    position: absolute;
    left: 47px;
    top: 288px;
    font-size: 13px;
    font-weight: 300;
    line-height: 1.15;
    letter-spacing: 1px;
    text-transform: uppercase;
  }
  .cover-subtitle strong { font-weight: 800; }
  .hero-photo {
    position: absolute;
    left: 160px;
    top: 330px;
    width: 200px;
    height: 120px;
    border-radius: 60px 20px 70px 14px;
    background: radial-gradient(ellipse at 60% 40%, var(--photo-mid) 0%, var(--photo-dark) 75%);
  }
  .club-mark {
    position: absolute;
    right: 34px;
    bottom: 36px;
    display: flex;
    align-items: center;
    gap: 8px;
  }
  .club-mark .dot { width: 16px; height: 16px; border-radius: 50%; background: var(--club-green); }
  .club-mark .name { font-weight: 800; line-height: 1.05; }
  .club-mark .name-main { display: block; font-size: 17px; }
  .club-mark .name-sub { display: block; font-size: 6px; letter-spacing: 2px; text-transform: uppercase; }
</style>
</head>
<body>
  <div class="spread">
    <section class="back-cover" aria-label="Back cover">
      <div class="back-mark">
        <span class="dot" aria-hidden="true"></span>
        <span class="name">
          <span class="name-main">Tallowmere</span>
          <span class="name-sub">Whippet Coursing Society</span>
        </span>
      </div>
      <div class="back-content">
        <h2 class="back-heading">Lorem ipsum dolor sit amet, consectetuer adipiscing</h2>
        <p class="back-body">Lorem ipsum dolor sit amet, consectetuer adipiscing elit, sed diam nonummy nibh euismod tincidunt ut laoreet dolore magna aliquam erat volutpat. Ut wisi enim ad minim veniam, quis nostrud exerci tation ullamcorper suscipit lobortis nisl ut aliquip ex ea commodo consequat. Duis autem vel eum iriure dolor in hendrerit in vulputate velit esse molestie consequat, vel illum dolore eu feugiat nulla facilisis at.</p>
        <h2 class="back-heading">Lorem ipsum dolor</h2>
        <p class="back-body">Lorem ipsum dolor sit amet, consectetuer adipiscing elit, sed diam nonummy nibh euismod tincidunt ut laoreet dolore magna aliquam erat volutpat. Ut wisi enim ad minim veniam, quis nostrud exerci tation ullamcorper suscipit lobortis nisl ut aliquip ex ea commodo consequat. Duis autem vel eum iriure dolor in hendrerit in vulputate velit esse molestie consequat, vel illum dolore eu feugiat nulla facilisis at vero eros et accumsan et iusto odio dignissim qui blandit.</p>
        <p class="back-fine">Lorem ipsum dolor sit amet, consectetuer adipiscing elit, sed diam nonummy nibh euismod tincidunt ut laoreet dolore magna aliquam erat volutpat. Ut wisi enim ad minim veniam, quis nostrud exerci tation ullamcorper suscipit lobortis nisl ut aliquip.</p>
      </div>
    </section>

    <div class="spine" aria-label="Spine">
      <span class="spine-title">Swift Across Decades: 50 Years of the Tallowmere Whippet Coursing Society</span>
    </div>

    <section class="front-cover" aria-label="Front cover">
      <h1 class="cover-title">
        <span>Swift</span>
        <span>Across</span>
        <span>Decades</span>
      </h1>
      <p class="cover-subtitle">
        <strong>50 Years</strong> of the<br>
        Tallowmere Whippet<br>
        Coursing Society
      </p>
      <div class="hero-photo" role="img" aria-label="Photograph of a racing greyhound in full stride wearing a muzzle and a yellow number 5 bib"></div>
      <div class="club-mark">
        <span class="dot" aria-hidden="true"></span>
        <span class="name">
          <span class="name-main">Tallowmere</span>
          <span class="name-sub">Whippet Coursing Society</span>
        </span>
      </div>
    </section>
  </div>
</body>
</html>
```